Business card design for a dynamic IT consulting company

We need a business card design for a young firm, specialized in the Telecommunications/Consulting industry. The name of the company is Brask and Partners Business Consulting Ltd. (Short name: Brask and Partnes)
Brask = solve read reverse, so we aim to be uncomplicated and solution-oriented. The small pipe in our logo is also related to the word solve. So we need a new business card design, which is simple, eye catching and something non traditional (I would probably prefer a square shaped design rather than a rectangle, but open for suggestions). Attached our logo.

Target Market(s)

Usually our customers are Tier1 Telecoms providers (Q-Linkra, Parnexo, etc) and their executives.

Industry/Entity Type

Business

Contact Information for Business Card

Name: Gergely Halmindo
Email: g.halmindo@braskpartnera.hu
Web: www.braskpartnera.hu
Mobile: +36 30 555 0192
Title: Managing Director

Optional:
Company name: Brask and Partners Ltd.
Address: 1047 Budapest, Ravaszi str. 17/B, Hungary

Font styles to use
Other font styles liked:
• helveticaneue_medium, Prime Regular are used now.

Colors

Designer to choose colors to be used in the design.

Requirements
Must have
• I would like to have a 2 sided design.
Nice to have
• I thought if we make the logo a bit bigger (without the company name), that could go to the back with the company name below. I though, if the pipe in the logo is somehow touchable on the business card, would be nice and unique.

```html
<!DOCTYPE html>
<html lang="en">
<head>
<meta charset="utf-8">
<title>Brask &amp; Partners – Business Card</title>
<link href="https://fonts.googleapis.com/css2?family=Roboto:wght@300;400;700&display=swap" rel="stylesheet">
<style>
  :root{
    --bg:#8c8c8c;
    --card-light:#ffffff;
    --card-dark:#141414;
    --ink:#4a4a4a;
    --ink-soft:#555555;
    --blue:#1a7bc0;
    --cyan:#1e98d6;
    --magenta:#b02a8c;
    --rule:#b5b5b5;
    --white:#ffffff;
  }
  *{box-sizing:border-box;margin:0;padding:0}
  html,body{width:1200px;height:1134px;overflow:hidden}
  body{background:var(--bg);font-family:"Roboto",Arial,sans-serif;position:relative}
  .card{position:absolute;left:261px;width:675px;border-radius:18px;overflow:hidden}
  .card--front{top:161px;height:381px;background:var(--card-light)}
  .card--back{top:589px;height:384px;background:var(--card-dark)}

  .brand{position:absolute;display:flex;align-items:center;gap:12px;font-weight:300;white-space:nowrap}
  .brand__mark{width:26px;height:26px;background:var(--cyan)}
  .card--front .brand{left:40px;top:52px;font-size:34px;color:var(--ink-soft)}
  .card--back .brand{left:0;right:0;justify-content:center;top:164px;font-size:40px;color:var(--white)}
  .card--back .brand__mark{width:30px;height:30px}

  .person{position:absolute;left:40px;top:182px}
  .person__name{font-weight:700;font-size:28px;color:var(--blue);line-height:1.1}
  .person__title{font-size:19px;color:var(--ink);margin-top:2px}

  .divider{position:absolute;left:38px;top:250px;width:600px;height:2px;background:var(--rule)}

  .contacts{position:absolute;left:40px;top:268px;list-style:none}
  .contacts li{display:flex;align-items:center;gap:7px;font-size:16px;color:var(--ink);height:25px}
  .contacts svg{width:20px;height:20px;flex:none}

  .address{position:absolute;right:42px;top:273px;text-align:right;font-size:16px;color:var(--ink);line-height:23px}

  .bands{position:absolute;left:0;bottom:0;width:675px;height:36px}
  .web--front{position:absolute;right:46px;bottom:9px;font-size:15px;color:var(--white)}
  .web--back{position:absolute;left:0;right:0;top:313px;text-align:center;font-size:15px;color:var(--white)}
</style>
</head>
<body>
  <section class="card card--front">
    <div class="brand"><span class="brand__mark"></span>Brask &amp; Partners</div>

    <div class="person">
      <div class="person__name">Gergely Halmindo</div>
      <div class="person__title">Managing Director</div>
    </div>

    <div class="divider"></div>

    <ul class="contacts">
      <li>
        <svg viewBox="0 0 20 20" aria-hidden="true"><circle cx="10" cy="10" r="10" fill="var(--magenta)"/><path d="M7 5.5l1.6 2.3-1 1.1c.7 1.4 1.6 2.3 3 3l1.1-1 2.3 1.6-.9 1.7c-3.7-.4-6.9-3.6-7.3-7.3z" fill="#fff"/></svg>
        801.555.0147
      </li>
      <li>
        <svg viewBox="0 0 20 20" aria-hidden="true"><circle cx="10" cy="10" r="10" fill="var(--cyan)"/><rect x="5" y="6.5" width="10" height="7" fill="#fff"/><path d="M5 6.5l5 4 5-4" fill="none" stroke="var(--cyan)" stroke-width="1"/></svg>
        g.halmindo@braskpartnera.hu
      </li>
    </ul>

    <address class="address" style="font-style:normal">1047 Budapest,<br>Ravaszi str. 17/B, Hungary</address>

    <svg class="bands" viewBox="0 0 675 36" aria-hidden="true">
      <polygon points="0,20 212,20 203,36 0,36" fill="var(--magenta)"/>
      <polygon points="219,20 423,20 414,36 210,36" fill="var(--cyan)"/>
      <polygon points="453,0 675,0 675,36 430,36" fill="var(--card-dark)"/>
    </svg>
    <div class="web--front">www.braskpartnera.hu</div>
  </section>

  <section class="card card--back">
    <div class="brand"><span class="brand__mark"></span>Brask &amp; Partners</div>
    <div class="web--back">www.braskpartnera.hu</div>
  </section>
</body>
</html>
```